New business card with our logo

we finalized our logo with the help of pixel harbor - now we need a business card using that logo. we are a metal service center providing raw steel and metal products for fabricating, contractors, artists, etc. we have the wording for the back of the card figured out (attached, no deviations from text please), just need help putting it all together.
would like the look of steel somehow incorporated in the design ... would like the black part of the logo to be steel or silver color (the S & BRANLEY)
Other font styles liked:
- calibri, arial, similar to those, modern looking
Colors
Designer to choose colors to be used in the design.
Requirements
Must have
- Back of card must haves are attached (no deviations from wording please).
- FRONT of card:
- logo
- address
- name
- office tel
- cell
- fax
- website
- address
Nice to have
- incorporate the look of steel or element of steel somehow
- names of the staff on front not in all caps, i.e. Rosvita not ROSVITA
- this industry is more industrial, not coffee or flower shop so design should be aligned with that
- design should be classic and tasteful

```html
<!DOCTYPE html>
<html lang="en">
<head>
<meta charset="utf-8">
<title>Branley Steel – Business Card</title>
<link href="https://fonts.googleapis.com/css2?family=Montserrat:wght@500;700;800&family=Lato:wght@400;700&display=swap" rel="stylesheet">
<style>
  :root{
    --bg:#e9eaec;
    --paper:#f4f4f5;
    --ink:#1d1e20;
    --blue:#1a72b8;
    --white:#f2f2f2;
    --silver-dark:#6d6f73;
    --silver-light:#e6e7e9;
  }
  *{margin:0;padding:0;box-sizing:border-box}
  html,body{width:1200px;height:1182px;overflow:hidden;background:var(--bg)}
  body{position:relative;font-family:"Lato",Arial,sans-serif}
  .card{position:absolute;left:150px;width:900px;height:514px;background:var(--paper);
        box-shadow:0 6px 24px rgba(0,0,0,.12);overflow:hidden}
  .card-back{top:52px}
  .card-front{top:616px}
  .card svg.card-bg{position:absolute;inset:0;width:100%;height:100%}
  .wordmark{position:absolute;display:flex;align-items:center;gap:16px}
  .wordmark-dot{width:58px;height:58px;border-radius:50%;border:5px solid var(--blue)}
  .wordmark-name{font-family:"Montserrat",Arial,sans-serif;font-weight:700;color:var(--blue);
        letter-spacing:2px;line-height:1}
  /* back */
  .services{position:absolute;left:46px;top:48px;list-style:none;color:var(--white);
        font-size:21px;line-height:1.45;letter-spacing:.5px}
  .services li::before{content:"";display:inline-block;width:6px;height:6px;border-radius:50%;
        background:var(--white);margin-right:12px;vertical-align:middle}
  .services-rule{position:absolute;left:46px;top:220px;width:340px;height:1px;background:#8a8c90}
  .card-back .wordmark{right:56px;top:86px}
  .card-back .wordmark-name{font-size:42px}
  .headline{position:absolute;right:56px;top:172px;text-align:right;font-family:"Montserrat",Arial,sans-serif}
  .headline-title{font-weight:800;font-size:28px;letter-spacing:2px;color:var(--ink)}
  .headline-sub{margin-top:6px;font-weight:500;font-size:19px;letter-spacing:1.5px;color:var(--blue)}
  .tagline{position:absolute;left:420px;top:455px;color:var(--blue);font-size:21px;letter-spacing:.5px;font-weight:700}
  /* front */
  .card-front .wordmark{left:56px;top:86px}
  .card-front .wordmark-name{font-size:44px;line-height:1.05}
  .contact{position:absolute;left:560px;top:74px;color:var(--white)}
  .contact-name{font-family:"Montserrat",Arial,sans-serif;font-weight:700;font-size:32px;color:var(--blue)}
  .contact-role{font-size:19px;margin-top:2px;letter-spacing:.5px}
  .contact-rule{width:44px;height:1px;background:#8a8c90;margin:16px 0}
  .contact-row{display:flex;gap:14px;font-size:18px;line-height:1.4;letter-spacing:.5px}
  .contact-row svg{flex:none;width:16px;height:16px;margin-top:4px}
  .contact-address{margin-bottom:0}
</style>
</head>
<body>

<section class="card card-back">
  <svg class="card-bg" viewBox="0 0 900 514" aria-hidden="true">
    <defs>
      <linearGradient id="steelBack" x1="0" y1="0" x2="1" y2="1">
        <stop offset="0" stop-color="var(--silver-light)"/>
        <stop offset=".45" stop-color="var(--silver-dark)"/>
        <stop offset=".7" stop-color="var(--silver-light)"/>
        <stop offset="1" stop-color="var(--silver-dark)"/>
      </linearGradient>
    </defs>
    <path d="M0,0 L200,0 C370,0 410,330 560,400 C660,448 780,455 900,425 L900,514 L0,514 Z" fill="var(--ink)"/>
    <path d="M200,0 C370,0 410,330 560,400 C660,448 780,455 900,425" fill="none" stroke="url(#steelBack)" stroke-width="12"/>
  </svg>
  <ul class="services">
    <li>Structural Steel</li>
    <li>Stainless &amp; Aluminum</li>
    <li>Building Components</li>
    <li>Rebar, Decking... and more!</li>
  </ul>
  <div class="services-rule"></div>
  <div class="wordmark">
    <span class="wordmark-dot"></span>
    <span class="wordmark-name">BRANLEY STEEL</span>
  </div>
  <div class="headline">
    <p class="headline-title">METAL SERVICE CENTER</p>
    <p class="headline-sub">CUT · SHEAR · PUNCH · LIGHT FAB</p>
  </div>
  <p class="tagline">Cut to size, Pick-up or Delivered!</p>
</section>

<section class="card card-front">
  <svg class="card-bg" viewBox="0 0 900 514" aria-hidden="true">
    <defs>
      <linearGradient id="steelFront" x1="0" y1="0" x2="0" y2="1">
        <stop offset="0" stop-color="var(--silver-light)"/>
        <stop offset=".5" stop-color="var(--silver-dark)"/>
        <stop offset=".8" stop-color="var(--silver-light)"/>
        <stop offset="1" stop-color="var(--silver-dark)"/>
      </linearGradient>
    </defs>
    <path d="M470,0 L900,0 L900,514 L220,514 C330,450 440,420 455,300 C468,200 458,80 470,0 Z" fill="var(--ink)"/>
    <path d="M470,0 C458,80 468,200 455,300 C440,420 330,450 220,514" fill="none" stroke="url(#steelFront)" stroke-width="12"/>
  </svg>
  <div class="wordmark">
    <span class="wordmark-dot"></span>
    <span class="wordmark-name">BRANLEY<br>STEEL</span>
  </div>
  <div class="contact">
    <p class="contact-name">Tobias Renner</p>
    <p class="contact-role">Managing Director</p>
    <div class="contact-rule"></div>
    <div class="contact-row contact-address">
      <svg viewBox="0 0 16 16"><path d="M8 1a5 5 0 0 1 5 5c0 4-5 9-5 9S3 10 3 6a5 5 0 0 1 5-5z" fill="none" stroke="var(--blue)" stroke-width="1.8"/><circle cx="8" cy="6" r="1.8" fill="var(--blue)"/></svg>
      <span>P.O. Box KR418<br>Harwick HW 2B<br>Easton, USA</span>
    </div>
    <div class="contact-rule"></div>
    <div class="contact-row">
      <svg viewBox="0 0 16 16"><rect x="4" y="1" width="8" height="14" rx="1.5" fill="none" stroke="var(--blue)" stroke-width="1.6"/></svg>
      <span>000 000 0000</span>
    </div>
    <div class="contact-row">
      <svg viewBox="0 0 16 16"><path d="M3 2l3 0 1 4-2 1c1 2 2 3 4 4l1-2 4 1 0 3c-7 1-12-4-11-11z" fill="var(--blue)"/></svg>
      <span>000 000 0000</span>
    </div>
    <div class="contact-row">
      <svg viewBox="0 0 16 16"><rect x="4" y="2" width="8" height="4" fill="none" stroke="var(--blue)" stroke-width="1.4"/><rect x="1" y="6" width="14" height="8" rx="1" fill="var(--blue)"/></svg>
      <span>000 000 0000</span>
    </div>
    <div class="contact-row">
      <svg viewBox="0 0 16 16"><rect x="1" y="3" width="14" height="10" fill="none" stroke="var(--blue)" stroke-width="1.5"/><path d="M1 3l7 6 7-6" fill="none" stroke="var(--blue)" stroke-width="1.5"/></svg>
      <span>tobias@branleysteel.com</span>
    </div>
    <div class="contact-row">
      <svg viewBox="0 0 16 16"><circle cx="8" cy="8" r="6.5" fill="none" stroke="var(--blue)" stroke-width="1.5"/><ellipse cx="8" cy="8" rx="3" ry="6.5" fill="none" stroke="var(--blue)" stroke-width="1.2"/><path d="M1.5 8h13" stroke="var(--blue)" stroke-width="1.2"/></svg>
      <span>www.branleysteel.com</span>
    </div>
  </div>
</section>

</body>
</html>
```